Exhibition Print

Need to have a few video meetings and work scope
we have approx 20 panels that need to tell a story of our business
I have updated a story board'
Our main company is:
velnori.com.au fibre to the home technologies for new or greenfield retirement estates and ethernet over copper for existing retirement estates

We will pay for the extra meetings on top

so the design needs approx 20 panels 2.4m HEIGHT x 1m WIDE
so we will work out the correct way to price this together

Target Market(s)

retirement communiites

Industry/Entity Type

retirement and communication technologies

Requirements
Nice to have
• i have attached a story board

```html
<!DOCTYPE html>
<html lang="en">
<head>
<meta charset="utf-8">
<title>Velnori Health – Exhibition Panels</title>
<link href="https://fonts.googleapis.com/css2?family=Poppins:wght@500;600;700&display=swap" rel="stylesheet">
<style>
  :root {
    --green: #52a548;
    --blue: #126eb6;
    --sky: #00aeef;
    --ink-blue: #1569b2;
    --white: #ffffff;
    --paper: #ffffff;
  }
  * { margin: 0; padding: 0; box-sizing: border-box; }
  html, body { width: 1200px; height: 1200px; overflow: hidden; background: var(--paper); }
  body { position: relative; font-family: 'Poppins', sans-serif; }

  .panel {
    position: absolute;
    top: 54px;
    height: 1065px;
    overflow: hidden;
    background: var(--blue);
    box-shadow: 2px 2px 3px rgba(0,0,0,.35);
  }
  .panel--connected { left: 122px; width: 444px; }
  .panel--journey { left: 648px; width: 441px; }
  .panel-bg { position: absolute; inset: 0; width: 100%; height: 100%; }

  .panel-title {
    position: absolute;
    color: var(--white);
    font-weight: 700;
    font-size: 50px;
    line-height: 56px;
    letter-spacing: -0.5px;
  }
  .panel--connected .panel-title { left: 72px; top: 100px; }
  .panel--journey .panel-title { left: 0; right: 0; top: 100px; text-align: center; }

  .intro {
    position: absolute;
    left: 53px; top: 325px; width: 360px;
    color: var(--white);
    font-weight: 600;
    font-size: 19.5px;
    line-height: 24px;
  }

  .art { position: absolute; }
  .art--video-call {
    left: 221px; top: 456px; width: 196px; height: 259px;
    background: linear-gradient(160deg, #00aeef 0%, #6fc3ea 45%, #a5a8bf 100%);
  }
  .art--laptop-user {
    left: 0; top: 499px; width: 325px; height: 453px;
    background: linear-gradient(160deg, #e4e4e4 0%, #d6ecf8 45%, #5f4a68 100%);
    border-radius: 140px 60px 0 0;
  }
  .art--bush { background: transparent; }

  .stat {
    position: absolute;
    height: 43px;
    background: var(--sky);
    color: var(--white);
    font-weight: 700;
    font-size: 20px;
    line-height: 43px;
    text-align: center;
    border-radius: 8px;
  }
  .stat--years { left: 174px; top: 361px; width: 129px; }
  .stat--services { left: 40px; top: 438px; width: 207px; }
  .stat--since { left: 170px; top: 513px; width: 207px; }

  .mission {
    position: absolute;
    left: 74px; top: 613px; width: 282px; height: 116px;
    background: var(--white);
    border-radius: 6px;
    box-shadow: 7px 8px 0 var(--sky);
    text-align: center;
  }
  .mission-tag {
    display: inline-block;
    margin-top: 13px;
    width: 118px; height: 30px;
    background: var(--green);
    color: var(--white);
    border-radius: 5px;
    font-weight: 700;
    font-size: 20px;
    line-height: 31px;
  }
  .mission-text {
    margin-top: 2px;
    color: var(--ink-blue);
    font-weight: 700;
    font-size: 20px;
    line-height: 25px;
  }
</style>
</head>
<body>

<section class="panel panel--connected">
  <svg class="panel-bg" viewBox="0 0 444 1065" preserveAspectRatio="none" aria-hidden="true">
    <rect width="444" height="1065" fill="var(--blue)"/>
    <path d="M0,0 H444 V177 C420,240 390,262 328,267 C260,272 200,268 141,273 C60,280 5,340 0,421 Z" fill="var(--green)"/>
    <rect x="0" y="864" width="444" height="201" fill="var(--sky)"/>
    <path d="M444,864 C400,960 280,1050 70,1065 H444 Z" fill="var(--green)"/>
  </svg>
  <h1 class="panel-title">We Keep You<br>Connected</h1>
  <p class="intro">Velnori Health keeps retirement communities connected through future-ready telecom and care solutions.</p>
  <div class="art art--video-call" role="img" aria-label="Illustration of an older man holding a phone during a video call"></div>
  <div class="art art--laptop-user" role="img" aria-label="Illustration of an older woman smiling while using a laptop"></div>
</section>

<section class="panel panel--journey">
  <svg class="panel-bg" viewBox="0 0 441 1065" preserveAspectRatio="none" aria-hidden="true">
    <rect width="441" height="1065" fill="var(--blue)"/>
    <path d="M0,0 H441 V256 L218,297 L0,256 Z" fill="var(--green)"/>
    <path d="M142.5,313 V421 Q142.5,456 164,456 H292.5 Q319,456 319,483 V577 Q319,607 283,607 H139 Q121,607 121,633"
          fill="none" stroke="var(--green)" stroke-width="25"/>
    <path d="M121,746 Q121,762 146,762 H296 Q322,762 322,789 V886 Q322,912 296,912 H219 Q193,912 193,939 V1002"
          fill="none" stroke="var(--green)" stroke-width="25"/>
  </svg>
  <h2 class="panel-title">Our Journey<br>&amp; Mission</h2>
  <div class="art art--bush" role="img" aria-label="Decorative shrubs along the path" style="left:60px;top:357px;width:330px;height:190px;position:absolute;"></div>
  <div class="stat stat--years">20+ years</div>
  <div class="stat stat--services">40,000+ services</div>
  <div class="stat stat--since">from 2004 to now</div>
  <div class="mission">
    <span class="mission-tag">Mission:</span>
    <p class="mission-text">Bridging distances,<br>connecting hearts</p>
  </div>
  <div class="art art--bush" role="img" aria-label="Decorative shrubs beside the path" style="left:103px;top:787px;width:160px;height:110px;position:absolute;"></div>
</section>

</body>
</html>
```